Book cover

I am working with my publisher to publish my book They came up with a book cover but I don't like it. I want to see different designs. The book Title is Shiftcraftery the subtitle How to Steer Upheaval with Focus, Poise & Resolve by Marilyn T. Hargreave
I want to use my Brand Colors including the blue. I am uploading the covers of my other book. This is a professional leadership book. The publisher will make the cover when providing them a new design. the Shiftcraftery one is one I played with on Canva. I would like more color and to incorporate the blue. I want a spot at the top where I can write a quote. Shiftcraftery is one word in the text so should be the same on the cover. I want the cover to show energy movement and am open to an image too. I am attaching logos for the feel of the brand and brand rgb codes.

```html
<!DOCTYPE html>
<html lang="en">
<head>
<meta charset="utf-8">
<title>Shiftcraftery — Book Cover</title>
<link rel="stylesheet" href="https://fonts.googleapis.com/css2?family=Anton&family=Jost:wght@300;500&display=swap">
<style>
  :root {
    --cover-red: #da2432;
    --brand-teal: #078f9b;
    --compass-dark: #1d3a40;
    --ink-white: #ffffff;
  }
  html, body {
    margin: 0;
    padding: 0;
    width: 800px;
    height: 1200px;
    overflow: hidden;
    background: var(--cover-red);
  }
  .book-cover {
    position: relative;
    width: 800px;
    height: 1200px;
    background: var(--cover-red);
    overflow: hidden;
  }
  .cover-art {
    position: absolute;
    inset: 0;
    width: 800px;
    height: 1200px;
  }
  .energy-stroke {
    stroke: var(--brand-teal);
  }
  .title-word {
    font-family: "Anton", "Impact", sans-serif;
    font-size: 135px;
    fill: var(--ink-white);
  }
  .quote-space {
    position: absolute;
    left: 60px;
    top: 50px;
    width: 680px;
    height: 300px;
  }
  .compass-visual {
    position: absolute;
    left: 535px;
    top: 690px;
    width: 250px;
    height: 250px;
    border-radius: 50%;
    background: radial-gradient(circle at 45% 45%, var(--brand-teal) 0%, var(--compass-dark) 62%, #9aa4a6 63%, #5f6a6c 100%);
  }
  .subtitle {
    position: absolute;
    left: 0;
    width: 800px;
    top: 968px;
    margin: 0;
    font-family: "Jost", sans-serif;
    font-weight: 300;
    font-size: 42px;
    line-height: 44px;
    letter-spacing: -1px;
    color: var(--ink-white);
    text-align: center;
  }
  .author {
    position: absolute;
    left: 0;
    width: 800px;
    top: 1112px;
    margin: 0;
    font-family: "Jost", sans-serif;
    font-weight: 500;
    font-size: 56px;
    line-height: 60px;
    letter-spacing: -2px;
    color: var(--ink-white);
    text-align: center;
  }
</style>
</head>
<body>
  <main class="book-cover">
    <svg class="cover-art" viewBox="0 0 800 1200" xmlns="http://www.w3.org/2000/svg" aria-labelledby="cover-title">
      <title id="cover-title">Shiftcraftery</title>
      <defs>
        <filter id="soft-edge" x="-20%" y="-20%" width="140%" height="140%">
          <feGaussianBlur stdDeviation="4"/>
        </filter>
      </defs>
      <line class="energy-stroke" x1="610" y1="70" x2="70" y2="1120" stroke-width="125" stroke-linecap="round" filter="url(#soft-edge)"/>
      <text class="title-word" transform="translate(12 640) scale(1 1.8)" x="0" y="0" textLength="776" lengthAdjust="spacingAndGlyphs">SHIFTCRAFTERY</text>
    </svg>

    <div class="quote-space" aria-hidden="true"></div>

    <div class="compass-visual" role="img" aria-label="Photograph of a silver pocket compass with a teal dial and needle"></div>

    <p class="subtitle">How to Steer Upheaval<br>with Focus, Poise &amp; Resolve</p>
    <p class="author">Marilyn T. Hargreave</p>
  </main>
</body>
</html>
```